We are a Yacht Charter Broker servicing VIP clients on booking sailing catamarans and motor yacht...

We are looking for a wildly creative website to attract high net worth clients to work with us in booking their dream yacht vacation. A site that you think is 5 years ahead of its time. Sexy, modern and unique. Our company name is BRELLAVON. Our colors are navy blue and silver.
BLUE:
RGBB 0/44/92
CMYC 100/86/36/31
SILVER:
RGB 152/163/173
CMYK 43/29/25/0

HEX 98a3ad

Target Market(s)

High net worth people in need of white glove brokerage serving in finding and booking their dream yacht for a vacation of a lifetime.

Coding

Coded - Design and coding required

Number of Pages Required

1 page

Requirements
Must have
• Mobile friendly.
• Wildly creative and different. A website that we would expect to see 5 years from now.
• Pictures of yachts and or people on yachts. Palm tree landscapes.
• pictures of high end food related to the VIP yacht experience.
Nice to have
• Anything you feel would sell the yacht charter experience.
Should not have
• Nothing comes to mind.

```html
<!DOCTYPE html>
<html lang="en">
<head>
<meta charset="utf-8">
<title>Brellavon Yacht Charter Broker</title>
<link rel="stylesheet" href="https://fonts.googleapis.com/css2?family=Roboto:wght@400;500;700&family=Open+Sans:ital,wght@0,400;0,600;1,400&display=swap">
<style>
:root{
  --navy:#002c5c;
  --navy-deep:#0b2450;
  --footer:#0f2a58;
  --silver:#98a3ad;
  --icon-bg:#8b949d;
  --ink:#333;
  --muted:#666;
  --light:#f1f1f1;
  --white:#fff;
}
*{box-sizing:border-box;margin:0;padding:0}
html,body{width:1200px;height:3232px;overflow:hidden}
body{font-family:"Open Sans",Arial,sans-serif;color:var(--ink);background:var(--white);position:relative}
section,header,footer{position:absolute;left:0;width:1200px}
.center{text-align:center}

/* header */
.site-header{top:0;height:100px;background:var(--white)}
.brand{position:absolute;left:97px;top:28px;font-family:"Roboto",sans-serif;font-weight:500;font-size:32px;letter-spacing:5px;color:var(--navy)}
.brand-tag{position:absolute;left:150px;top:66px;font-family:"Roboto",sans-serif;font-size:9px;letter-spacing:2px;color:var(--navy)}
.main-nav a{position:absolute;top:42px;font-family:"Roboto",sans-serif;font-size:13px;color:#222;text-decoration:none}
.main-nav a.active{color:var(--navy);border-bottom:1px solid var(--navy);padding-bottom:6px}

/* hero */
.hero{top:100px;height:702px;background:var(--light)}
.hero-photo{position:absolute;left:0;top:0;width:1200px;height:600px;background:linear-gradient(180deg,#8a7a6a 0%,#c9a27a 30%,#a6a49f 48%,#e6e2dc 58%,#5b6f80 72%,#2d4256 100%)}
.hero-wave{position:absolute;left:0;top:520px}
.hero h1{position:absolute;top:162px;width:100%;font-family:"Roboto",sans-serif;font-weight:700;font-size:52px;color:var(--white);text-shadow:0 2px 6px rgba(0,0,0,.35)}
.hero-sub{position:absolute;top:224px;width:100%;font-size:16px;color:#f3eee8}
.btn-navy{background:var(--navy);color:var(--white);font-family:"Roboto",sans-serif;font-size:13px;border-radius:3px;display:flex;align-items:center;justify-content:center;gap:6px}
.hero .read-more{position:absolute;left:536px;top:271px;width:128px;height:38px}
.arrow-btn{position:absolute;top:237px;width:46px;height:46px;border-radius:50%;background:rgba(255,255,255,.25);display:flex;align-items:center;justify-content:center}
.search-bar .field{position:absolute;top:634px;height:36px;background:var(--white);border:1px solid #ddd;border-radius:3px;font-size:11px;color:#555;display:flex;align-items:center;padding:0 14px;justify-content:space-between}
.search-bar .go{position:absolute;left:967px;top:634px;width:112px;height:36px;font-weight:500}

/* welcome */
.welcome{top:802px;height:517px}
.section-title{font-family:"Roboto",sans-serif;font-weight:700;font-size:34px}
.welcome h2{position:absolute;top:60px;width:100%;color:var(--navy)}
.welcome .lead{position:absolute;left:151px;top:116px;width:904px;font-size:11px;line-height:20px;color:var(--muted)}
.feature{position:absolute;top:208px;width:300px;text-align:center}
.feature .ico{width:112px;height:112px;border-radius:50%;background:var(--icon-bg);margin:0 auto;display:flex;align-items:center;justify-content:center;border:3px solid #e1e4e7}
.feature h3{font-family:"Roboto",sans-serif;font-weight:400;font-size:21px;color:#333;margin-top:20px}
.feature p{font-size:11px;line-height:20px;color:var(--muted);margin-top:10px}

/* about */
.about{top:1319px;height:455px;background:linear-gradient(180deg,#6f8ba6 0%,#9fb3c3 22%,#3f6f96 36%,#1f5a8a 55%,#133f6e 100%)}
.about h2{position:absolute;top:138px;width:100%;color:var(--white);font-size:40px}
.about p{position:absolute;left:183px;top:199px;width:834px;font-size:12px;line-height:20px;color:var(--white)}
.btn-outline{position:absolute;left:455px;top:291px;width:290px;height:38px;border:2px solid var(--white);color:var(--white);font-family:"Roboto",sans-serif;font-size:16px;display:flex;align-items:center;justify-content:center}

/* services */
.services{top:1774px;height:597px}
.services h2{position:absolute;top:60px;width:100%;color:#2b2b2b}
.card{position:absolute;top:151px;width:236px;height:349px;background:var(--white);box-shadow:0 1px 5px rgba(0,0,0,.22)}
.card .photo{height:193px;position:relative}
.card .photo span{position:absolute;left:11px;bottom:10px;font-family:"Roboto",sans-serif;font-weight:700;font-size:14px;color:var(--white)}
.card p{padding:14px 11px 0;font-size:11px;line-height:20px;color:#444;height:96px}
.card .price{border-top:1px solid #e2e2e2;margin:0 11px;padding-top:12px;display:flex;justify-content:space-between;align-items:center}
.card .price small{display:block;font-family:"Roboto",sans-serif;font-size:10px;color:#333}
.card .price b{font-weight:400;font-size:15px;color:#333}
.card .btn-navy{width:80px;height:22px;font-size:9px}

/* testimonials */
.testimonials{top:2371px;height:527px;background:linear-gradient(180deg,#234f8a 0%,#1e477e 50%,#173a6c 100%)}
.testimonials h2{position:absolute;top:80px;width:100%;color:var(--white)}
.quote-box{position:absolute;left:142px;top:219px;width:916px;height:181px;border:2px solid rgba(255,255,255,.85);text-align:center;color:var(--white)}
.quote-box h4{margin-top:56px;font-family:"Roboto",sans-serif;font-size:16px;font-weight:700}
.quote-box h4 span{font-weight:400}
.quote-box p{margin:12px auto 0;width:800px;font-style:italic;font-size:12px;line-height:22px}
.avatar{position:absolute;left:546px;top:161px;width:108px;height:108px;border-radius:50%;border:4px solid #dfe6ee;background:radial-gradient(circle at 50% 45%,#b0896f,#5b4a66 70%)}
.dots{position:absolute;top:420px;width:100%;display:flex;justify-content:center;gap:7px}
.dots i{width:10px;height:10px;border-radius:50%;border:1.5px solid var(--white);background:var(--white)}
.dots i:first-child{background:transparent}
.testi-wave{position:absolute;left:0;top:470px}

/* footer */
.site-footer{top:2898px;height:334px;background:var(--footer);color:var(--white)}
.f-col{position:absolute;top:50px}
.f-col h5{font-family:"Roboto",sans-serif;font-weight:400;font-size:16px;margin-bottom:18px;letter-spacing:.5px}
.f-col li{list-style:none;font-size:13px;line-height:30px}
.f-col li svg{vertical-align:-2px;margin-right:10px}
.social{display:flex;gap:6px;margin-top:16px}
.social i{width:36px;height:36px;border-radius:50%;border:2px solid var(--white)}
.copyright{position:absolute;left:99px;right:99px;top:263px;border-top:1px solid rgba(255,255,255,.5);padding-top:20px;font-size:12px}
</style>
</head>
<body>

<header class="site-header">
  <div class="brand">BRELLAVON</div>
  <div class="brand-tag">YACHT CHARTER BROKER</div>
  <nav class="main-nav">
    <a class="active" style="left:484px">HOME</a>
    <a style="left:560px">ABOUT US</a>
    <a style="left:659px">OUR SERVICES</a>
    <a style="left:786px">YACHT VACATION</a>
    <a style="left:930px">GALLERY</a>
    <a style="left:1024px">CONTACT US</a>
  </nav>
</header>

<section class="hero">
  <div class="hero-photo" role="img" aria-label="Marina at sunset with luxury motor yachts moored on calm water"></div>
  <svg class="hero-wave" width="1200" height="90" viewBox="0 0 1200 90" aria-hidden="true">
    <path d="M0 80 C260 20 520 -10 800 40 C950 65 1080 60 1200 30 L1200 90 L0 90Z" fill="#e6ebef"/>
    <path d="M0 90 C260 35 520 10 800 55 C950 78 1080 72 1200 45 L1200 90Z" fill="#f1f1f1"/>
  </svg>
  <h1 class="center">BRELLAVON YACHT CHARTER BROKER</h1>
  <p class="hero-sub center">Sed ut perspiciatis unde omnis iste natus error sit voluptatem accusantium doloremque laudantium, totam</p>
  <div class="btn-navy read-more">READ MORE
    <svg width="12" height="12" viewBox="0 0 12 12"><circle cx="6" cy="6" r="6" fill="#fff"/><path d="M5 3l3 3-3 3" stroke="#002c5c" stroke-width="1.6" fill="none"/></svg>
  </div>
  <div class="arrow-btn" style="left:20px"><svg width="14" height="20"><path d="M11 2L3 10l8 8" stroke="#fff" stroke-width="2" fill="none"/></svg></div>
  <div class="arrow-btn" style="left:1134px"><svg width="14" height="20"><path d="M3 2l8 8-8 8" stroke="#fff" stroke-width="2" fill="none"/></svg></div>

  <div class="search-bar">
    <div class="field" style="left:112px;width:271px"><span>
      <svg width="8" height="11" viewBox="0 0 8 11"><path d="M4 0a4 4 0 014 4c0 3-4 7-4 7S0 7 0 4a4 4 0 014-4z" fill="#555"/><circle cx="4" cy="4" r="1.5" fill="#fff"/></svg>
      Choose Your Destination</span><svg width="8" height="5"><path d="M0 0h8L4 5z" fill="#555"/></svg></div>
    <div class="field" style="left:399px;width:269px"><span>Choose Departure Date</span>
      <svg width="12" height="12"><rect x="1" y="2" width="10" height="9" fill="none" stroke="#555"/><path d="M1 5h10M4 0v3M8 0v3" stroke="#555"/></svg></div>
    <div class="field" style="left:683px;width:271px"><span>Choose Ticket type</span><svg width="8" height="5"><path d="M0 0h8L4 5z" fill="#555"/></svg></div>
    <div class="btn-navy go">SEARCH</div>
  </div>
</section>

<section class="welcome">
  <h2 class="section-title center">WELCOME TO BRELLAVON</h2>
  <p class="lead center">Sed ut perspiciatis unde omnis iste natus error sit voluptatem accusantium doloremque laudantium, totam rem aperiam, eaque ipsa quae ab illo inventore veritatis et quasi architecto beatae vitae dicta sunt explicabo. Nemo enim ipsam voluptatem quia voluptas sit aspernatur aut odit aut fugit, sed quia consequuntur magni dolores eos qui ratione voluptatem sequi nesciunt. Neque porro quisquam est, qui dolorem ipsum quia dolor sit amet, consectetur, adipisci velit,</p>

  <div class="feature" style="left:104px">
    <div class="ico"><svg width="52" height="52" viewBox="0 0 52 52" fill="none" stroke="#fff" stroke-width="3">
      <rect x="4" y="8" width="36" height="32" rx="2"/><path d="M4 17h36M12 3v9M32 3v9"/><circle cx="38" cy="38" r="11" fill="#8b949d"/><path d="M38 32v6l4 3"/></svg></div>
    <h3>Events Booking</h3>
    <p>Nemo enim ipsam voluptatem quia voluptas sit<br>aspernatur aut odit aut fugit, sed quia consequuntur<br>magni dolores eos qui ratione voluptatem</p>
  </div>
  <div class="feature" style="left:445px">
    <div class="ico"><svg width="60" height="40" viewBox="0 0 60 40" fill="#fff">
      <path d="M2 24h56l-8 10H10z"/><path d="M14 24l6-9h22l6 9z"/><path d="M22 15l4-6h10l2 6z"/><path d="M2 38c6-3 10-3 14 0s10 3 14 0 10-3 14 0 10 3 14 0" stroke="#fff" stroke-width="2" fill="none"/></svg></div>
    <h3>Yacht Vacation</h3>
    <p>Nemo enim ipsam voluptatem quia voluptas sit<br>aspernatur aut odit aut fugit, sed quia consequuntur<br>magni dolores eos qui ratione voluptatem</p>
  </div>
  <div class="feature" style="left:785px">
    <div class="ico"><svg width="52" height="46" viewBox="0 0 52 46" fill="none" stroke="#fff" stroke-width="3">
      <path d="M4 34c6-4 10-4 16 0s10 4 16 0 10-4 14 0"/><path d="M4 42c6-4 10-4 16 0s10 4 16 0 10-4 14 0"/><path d="M10 26h32"/><path d="M26 6v20"/></svg></div>
    <h3>Getting here and away</h3>
    <p>Nemo enim ipsam voluptatem quia voluptas sit<br>aspernatur aut odit aut fugit, sed quia consequuntur<br>magni dolores eos qui ratione voluptatem</p>
  </div>
</section>

<section class="about" role="img" aria-label="Aerial view of a beachfront city skyline and open blue sea">
  <h2 class="section-title center">ABOUT BRELLAVON</h2>
  <p class="center">Nemo enim ipsam voluptatem quia voluptas sit aspernatur aut odit aut fugit, sed quia consequuntur magni dolores eos qui ratione voluptatem sequi nesciunt. Neque porro quisquam est, qui dolorem ipsum quia dolor sit amet, consectetur. Nemo enim ipsam voluptatem quia voluptas sit aspernatur aut odit aut fugit, sed quia consequuntur magni dolores eos qui ratione voluptatem sequi nesciunt. Neque porro</p>
  <div class="btn-outline">READ MORE INFORMATION</div>
</section>

<section class="services">
  <h2 class="section-title center">BRELLAVON SERVICES</h2>

  <article class="card" style="left:99px">
    <div class="photo" role="img" aria-label="Guest relaxing on the deck of a yacht" style="background:linear-gradient(160deg,#3a86c6,#1c5b92 55%,#c9c2b4)"><span>NOSTRUM EXERCITATION</span></div>
    <p>The standard chunk of Lorem Ipsum used since the 1500s is reproduced below for those interested.</p>
    <div class="price"><div><small>STARTS FROM</small><b>$250</b></div><div class="btn-navy">VIEW DETAILS</div></div>
  </article>
  <article class="card" style="left:353px">
    <div class="photo" role="img" aria-label="Sailing yacht rigging and winch at sea" style="background:linear-gradient(160deg,#7fa8cf,#4c7ea9 50%,#8a6a4a)"><span>MAGNI DOLORES EOS</span></div>
    <p>The standard chunk of Lorem Ipsum used since the 1500s is reproduced below for those interested.</p>
    <div class="price"><div><small>STARTS FROM</small><b>$250</b></div><div class="btn-navy">VIEW DETAILS</div></div>
  </article>
  <article class="card" style="left:608px">
    <div class="photo" role="img" aria-label="Motor yachts docked in a harbour" style="background:linear-gradient(160deg,#b7c9d8,#e8ecef 45%,#2f6b8f)"><span>PORRO QUISQUAM EST</span></div>
    <p>The standard chunk of Lorem Ipsum used since the 1500s is reproduced below for those interested.</p>
    <div class="price"><div><small>STARTS FROM</small><b>$250</b></div><div class="btn-navy">VIEW DETAILS</div></div>
  </article>
  <article class="card" style="left:864px">
    <div class="photo" role="img" aria-label="Superyacht anchored near rocky cliffs" style="background:linear-gradient(160deg,#8fa2a6,#5f7a7f 45%,#1f5f86)"><span>VOLUPTATE VELIT ESSE</span></div>
    <p>The standard chunk of Lorem Ipsum used since the 1500s is reproduced below for those interested.</p>
    <div class="price"><div><small>STARTS FROM</small><b>$250</b></div><div class="btn-navy">VIEW DETAILS</div></div>
  </article>
</section>

<section class="testimonials" role="img" aria-label="Marina with moored boats under a navy overlay">
  <h2 class="section-title center">CLIENT TESTIMONIALS</h2>
  <div class="quote-box">
    <h4>Molestiae Conse <span>(City Name)</span></h4>
    <p>At vero eos et accusamus et iusto odio dignissimos ducimus qui blanditiis praesentium voluptatum deleniti atque corrupti quos dolores et quas molestias excepturi sint occaecati cupiditate non provident.</p>
  </div>
  <div class="avatar" role="img" aria-label="Client portrait"></div>
  <div class="dots"><i></i><i></i><i></i></div>
  <svg class="testi-wave" width="1200" height="57" viewBox="0 0 1200 57" aria-hidden="true">
    <path d="M0 57 L0 30 C300 0 600 10 850 35 C1000 50 1110 30 1200 10 L1200 57Z" fill="#c8d2dd"/>
    <path d="M0 57 L0 40 C300 10 600 20 850 45 C1000 58 1110 40 1200 22 L1200 57Z" fill="#0f2a58"/>
  </svg>
</section>

<footer class="site-footer">
  <div class="f-col" style="left:99px"><h5>COMPANY</h5>
    <ul><li>Home</li><li>About Us</li><li>Blog</li><li>News</li><li>Tours</li></ul></div>
  <div class="f-col" style="left:276px"><h5>SERVICES</h5>
    <ul><li>Tours</li><li>Places</li><li>Boat</li><li>Restaurants</li><li>Others</li></ul></div>
  <div class="f-col" style="left:498px"><h5>GET IN TOUCH</h5>
    <ul>
      <li><svg width="10" height="13" viewBox="0 0 8 11"><path d="M4 0a4 4 0 014 4c0 3-4 7-4 7S0 7 0 4a4 4 0 014-4z" fill="#fff"/></svg>Brellavon No 1207 Harbor Lane,</li>
      <li style="padding-left:20px;line-height:18px;margin-top:-6px;margin-bottom:6px">Bayview, MO 64810</li>
      <li><svg width="12" height="12" viewBox="0 0 12 12"><path d="M2 0l3 3-1.5 2a8 8 0 003.5 3.5L9 7l3 3-2 2C5 12 0 7 0 2z" fill="#fff"/></svg>Call us on (01) 55501234</li>
      <li><svg width="13" height="10" viewBox="0 0 13 10"><rect width="13" height="10" fill="#fff"/><path d="M0 0l6.5 5L13 0" stroke="#0f2a58" fill="none"/></svg>hello@brellavon.example</li>
    </ul></div>
  <div class="f-col" style="left:769px"><h5>WHY US</h5>
    <ul><li>Customers</li><li>Team</li><li>FAQ</li><li>Contact</li></ul></div>
  <div class="f-col" style="left:924px"><h5>FOLLOW US</h5>
    <ul><li>Please connect with us on</li></ul>
    <div class="social"><i style="background:#3ba3e0"></i><i style="background:#3b5aa0"></i><i style="background:#1d7ab5"></i><i style="background:#d5412f"></i></div></div>
  <div class="copyright">© 2018 Brellavon.&nbsp; All right reserved.&nbsp; Term of Use</div>
</footer>

</body>
</html>
```